Business Card design

I would like to redo the business cards we have. I want a group card and then individual cards made for each doctor. I like the format of the card attached.

```html
<!DOCTYPE html>
<html lang="en">
<head>
<meta charset="utf-8">
<title>Garden Valley Oncology – Business Cards</title>
<link href="https://fonts.googleapis.com/css2?family=Lato:wght@400;700&display=swap" rel="stylesheet">
<style>
  :root {
    --backdrop: #2b2e33;
    --card: #ffffff;
    --navy: #0f4f86;
    --sky: #2a8fd0;
    --rule: #7aa6c8;
    --ink: #4a4a4a;
  }
  * { margin: 0; padding: 0; box-sizing: border-box; }
  html, body { width: 1200px; height: 952px; overflow: hidden; }
  body {
    background: var(--backdrop);
    font-family: "Lato", Arial, sans-serif;
    display: flex;
    align-items: center;
    justify-content: center;
    gap: 40px;
  }
  .card {
    width: 540px;
    height: 309px;
    background: var(--card);
    position: relative;
    box-shadow: 0 6px 18px rgba(0,0,0,.35);
  }
  .brand {
    display: flex;
    align-items: center;
    gap: 12px;
    color: var(--navy);
    font-weight: 700;
  }
  .brand-mark {
    width: 22px;
    height: 22px;
    background: var(--sky);
    flex: none;
  }
  /* Front side */
  .card--front {
    display: flex;
    align-items: center;
    justify-content: center;
  }
  .card--front .brand { font-size: 27px; }
  /* Contact side */
  .card--contact .brand {
    position: absolute;
    left: 0; right: 0;
    top: 52px;
    justify-content: center;
    font-size: 24px;
  }
  .doctor-name {
    position: absolute;
    left: 150px;
    top: 118px;
    font-size: 22px;
    font-weight: 700;
    color: var(--navy);
  }
  .credential-rule {
    position: absolute;
    left: 0; right: 0;
    top: 160px;
    height: 1px;
    background: var(--rule);
  }
  .credential {
    position: absolute;
    left: 150px;
    top: 150px;
    padding: 0 8px;
    background: var(--card);
    font-size: 15px;
    color: var(--sky);
    font-weight: 400;
    line-height: 20px;
  }
  .contact {
    position: absolute;
    left: 60px;
    top: 188px;
    font-size: 14px;
    color: var(--ink);
    line-height: 24px;
  }
  .contact .sep {
    display: inline-block;
    width: 6px; height: 6px;
    background: var(--sky);
    margin: 0 8px 2px;
    vertical-align: middle;
  }
</style>
</head>
<body>
  <section class="card card--front" aria-label="Card front">
    <div class="brand"><span class="brand-mark"></span><span>Garden Valley Oncology, PA</span></div>
  </section>

  <section class="card card--contact" aria-label="Card back">
    <div class="brand"><span class="brand-mark"></span><span>Garden Valley Oncology, PA</span></div>
    <p class="doctor-name">Leila Marsh</p>
    <div class="credential-rule"></div>
    <span class="credential">M.D.</span>
    <div class="contact">
      <p>418 Linden Park Road<span class="sep"></span>Westbrook, New Jersey 07100</p>
      <p>(555) 014-2290<span class="sep"></span>Fax (555) 014-2291</p>
    </div>
  </section>
</body>
</html>
```